Velvet Harbor Nose Picks - our own unique product line of cotton swabs

We have something now that we are not too happy with. Looking to create a label for a line of cotton swabs that we have created and designed to clean your nose from mucus and boogers. The logo that i have so far for the packaging is the white background with the black silhouette nose (attached). We need something that can do well in the retail/consumer market. Our website address (even though it is not live yet) should be listed somewhere on the label....
www.VelvetHarbor-example.com ( we sell pillows, but we have other product lines)
We would also like to see a brief description on how to correctly use the nose pick on the back side of the label. The description on how to use should read " insert cotton nose pick into nostril and give it a few counter clock wise twirls or till you feel mucus/debris latch onto the cotton. You may need to repeat the process and use more than one nose pick to achieve desired result."
As well as a warning mentioning : "Never insert plastic end of nose pick into any part of your body. Be careful and use with caution."
Also for you to know, the cotton is made from 100% natural cotton, the cotton head itself is thick and highly absorbent making it a pleasure to use. There are 50 nose picks per pack.
We're fine with keeping it simple and not making the packaging too busy, however we're open to your ideas and designs! I have given you the most important information relevant to the project. If there are any questions or something is not clear enough please kindly message me.

Requirements
Must have
• professional looking
clean looking
not busy
Should not have
• words clumping together making it appear as too much text in one area
too much text clumped together on the design

```html
<!DOCTYPE html>
<html lang="en">
<head>
<meta charset="utf-8">
<title>Velvet Harbor Nose Picks – Label</title>
<link rel="stylesheet" href="https://fonts.googleapis.com/css2?family=Montserrat:wght@400;500;600;700;800&family=Kaushan+Script&display=swap">
<style>
  :root {
    --teal: #40bfb5;
    --teal-soft: #72cbc3;
    --teal-pale: #e3f4f2;
    --grey: #7a8387;
    --grey-dark: #6b7478;
    --paper: #ffffff;
    --stage: #f2f3f3;
    --frame: #9aa1a4;
  }
  * { box-sizing: border-box; margin: 0; padding: 0; }
  html, body { width: 1200px; height: 589px; overflow: hidden; }
  body {
    background: var(--stage);
    font-family: "Montserrat", Arial, sans-serif;
    position: relative;
  }

  /* ---------- front label ---------- */
  .front-label {
    position: absolute; left: 40px; top: 82px;
    width: 566px; height: 424px;
    background: var(--paper);
    border: 1px solid var(--frame);
    overflow: hidden;
  }
  .brand-name {
    position: absolute; left: 40px; top: 40px;
    display: flex; align-items: center; gap: 12px;
    font-size: 40px; font-weight: 500; color: var(--grey);
    letter-spacing: 0.5px; line-height: 1;
  }
  .brand-dot {
    width: 14px; height: 14px; border-radius: 50%;
    background: var(--teal);
  }
  .cotton-badge {
    position: absolute; left: 426px; top: 0;
    width: 103px; height: 137px;
    background: var(--teal-soft);
    border-radius: 0 0 52px 52px;
  }
  .nose-art {
    position: absolute; left: 22px; top: 130px;
    width: 90px; height: 232px;
    background: linear-gradient(160deg, #eef0f1 0%, #d9dee0 100%);
    border-radius: 6px;
  }
  .material-line {
    position: absolute; left: 139px; top: 172px;
    font-size: 17px; font-weight: 700; color: var(--grey-dark);
    letter-spacing: 2.2px; line-height: 20px;
  }
  .title-band {
    position: absolute; left: 115px; top: 196px;
    width: 451px; height: 80px;
    background: var(--teal);
    color: var(--paper);
    text-align: center;
    padding-left: 30px;
  }
  .product-title {
    font-size: 48px; font-weight: 800; letter-spacing: 3px;
    line-height: 48px; margin-top: 8px;
  }
  .product-purpose {
    font-size: 12.4px; font-weight: 700; letter-spacing: 0.2px;
    line-height: 14px; margin-top: 5px;
  }
  .tagline {
    position: absolute; left: 206px; top: 282px;
    font-family: "Kaushan Script", cursive;
    font-size: 27px; line-height: 36px; color: var(--grey-dark);
  }
  .tagline-rule {
    position: absolute; left: 170px; top: 323px;
    width: 367px; height: 5px;
    background: var(--grey);
  }
  .pack-count {
    position: absolute; right: 44px; top: 336px;
    text-align: center; color: var(--grey-dark); line-height: 1;
  }
  .pack-count .count-number { display: block; font-size: 50px; font-weight: 800; }
  .pack-count .count-word { display: block; font-size: 21px; font-weight: 700; margin-top: -2px; }
  .site-url {
    position: absolute; left: 39px; top: 382px;
    font-size: 17px; font-weight: 500; color: var(--teal);
    letter-spacing: 1.1px; line-height: 20px;
  }

  /* ---------- back label ---------- */
  .back-label {
    position: absolute; left: 646px; top: 181px;
    width: 509px; height: 226px;
    background: var(--paper);
    border: 1px solid var(--frame);
  }
  .step-icons {
    position: absolute; left: 37px; top: 14px;
    display: flex; flex-direction: column; gap: 6px;
  }
  .step-icon {
    width: 63px; height: 63px; border-radius: 50%;
    border: 3px solid var(--teal);
    background: var(--teal-pale);
  }
  .usage {
    position: absolute; left: 119px; top: 26px; width: 352px;
  }
  .usage-heading {
    display: flex; align-items: center; gap: 6px;
    font-size: 15px; font-weight: 700; color: var(--teal);
    letter-spacing: 1px; white-space: nowrap; line-height: 18px;
  }
  .usage-heading::before, .usage-heading::after {
    content: ""; flex: 1; height: 3px;
    background-image: radial-gradient(circle, var(--teal) 0.9px, transparent 1.1px);
    background-size: 3.5px 3px;
  }
  .usage-steps {
    margin-top: 11px;
    font-size: 13.4px; line-height: 20px; color: var(--grey);
    text-align: justify; text-align-last: left;
  }
  .usage-warning {
    margin-top: 14px;
    background: var(--teal); color: var(--paper);
    border-radius: 8px;
    font-size: 12px; font-weight: 500; line-height: 16px;
    text-align: center; padding: 3px 10px;
  }
</style>
</head>
<body>

<section class="front-label" aria-label="Front label">
  <div class="brand-name"><span>Velvet Harbor</span><span class="brand-dot"></span></div>
  <div class="cotton-badge" role="img" aria-label="Natural cotton, highly absorbent badge"></div>
  <div class="nose-art" role="img" aria-label="Line illustration of a nose in profile with a cotton swab"></div>
  <p class="material-line">100% NATURAL COTTON</p>
  <div class="title-band">
    <h1 class="product-title">NOSE PICKS</h1>
    <p class="product-purpose">CLEAN YOUR NOSE FROM MUCUS AND BOOGERS</p>
  </div>
  <p class="tagline">How do you pick your nose?</p>
  <div class="tagline-rule"></div>
  <p class="pack-count"><span class="count-number">50</span><span class="count-word">count</span></p>
  <p class="site-url">www.VelvetHarbor-example.com</p>
</section>

<section class="back-label" aria-label="Back label">
  <div class="step-icons">
    <div class="step-icon" role="img" aria-label="Step 1: cotton pick inserted into nostril"></div>
    <div class="step-icon" role="img" aria-label="Step 2: twirling the pick counter clockwise"></div>
    <div class="step-icon" role="img" aria-label="Step 3: removing the pick with debris on cotton"></div>
  </div>
  <div class="usage">
    <h2 class="usage-heading">HOW TO USE</h2>
    <p class="usage-steps">Insert cotton nose pick into nostril and give it a few counter clockwise twirls or till you feel mucus/debris latch onto the cotton. You may need to repeat the process and use more than one nose pick to achieve desired result.</p>
    <p class="usage-warning">Never insert plastic end of nose pick into any part of your body. Be careful and use with caution.</p>
  </div>
</section>

</body>
</html>
```